" Empresa jovem, em franca expansao, com necessidade de ampliar e qualificar sua carteira de clientes, buscando aprimorar sua identidade visual para se destacar em uma concorrência com pouco investimento nesse fundamento corporativo e potencializar sua apresentaçao a clientes de grande porte. "

```html
<!DOCTYPE html>
<html lang="pt-BR">
<head>
<meta charset="UTF-8">
<title>Afiadora Serrana – Papel timbrado</title>
<link href="https://fonts.googleapis.com/css2?family=Open+Sans:wght@400;700&display=swap" rel="stylesheet">
<style>
  :root {
    --backdrop: #e6e3df;
    --paper: #ffffff;
    --navy: #1d3a5c;
    --green: #1c9a4b;
    --accent-grey: #e4e5e7;
    --accent-grey-light: #ecedee;
    --text-grey: #4a4f55;
  }
  html, body {
    margin: 0;
    padding: 0;
    width: 1200px;
    height: 1200px;
    overflow: hidden;
    background: var(--backdrop);
  }
  .canvas {
    position: relative;
    width: 1200px;
    height: 1200px;
  }
  .letterhead {
    position: absolute;
    left: 240px;
    top: 108px;
    width: 744px;
    height: 996px;
    background: var(--paper);
    box-shadow: 0 4px 18px rgba(0,0,0,0.25);
    overflow: hidden;
    font-family: "Open Sans", Arial, sans-serif;
  }
  .brand {
    position: absolute;
    top: 6px;
    left: 0;
    width: 100%;
    display: flex;
    flex-direction: column;
    align-items: center;
  }
  .brand-square {
    width: 36px;
    height: 36px;
    background: var(--navy);
  }
  .brand-name {
    margin-top: 44px;
    font-weight: 700;
    font-size: 21px;
    line-height: 24px;
    letter-spacing: 1px;
    color: var(--navy);
    text-transform: uppercase;
  }
  .decor-area {
    position: absolute;
    left: 0;
    top: 588px;
    width: 336px;
    height: 360px;
    background: linear-gradient(180deg, var(--accent-grey-light) 0%, var(--accent-grey) 100%);
    clip-path: polygon(0 96px, 336px 0, 336px 180px, 180px 360px, 0 360px);
  }
  .contact {
    position: absolute;
    left: 0;
    top: 924px;
    width: 100%;
    padding-left: 28px;
    box-sizing: border-box;
    text-align: center;
    color: var(--text-grey);
    font-size: 12px;
    line-height: 24px;
  }
  .contact p { margin: 0; }
  .footer-band {
    position: absolute;
    left: 96px;
    bottom: 5px;
    width: 564px;
    height: 14px;
    background: var(--green);
    border-radius: 7px 7px 0 0;
  }
</style>
</head>
<body>
  <div class="canvas">
    <div class="letterhead">
      <header class="brand">
        <div class="brand-square"></div>
        <div class="brand-name">Afiadora Serrana</div>
      </header>

      <div class="decor-area" role="img" aria-label="Faixa decorativa cinza clara com formas geométricas inclinadas"></div>

      <footer class="contact">
        <p class="contact-address">Rua das Oficinas, 410 Centro - Vale Alto&nbsp; MG - 34 5550-0147</p>
        <p class="contact-web">www.afiadoraserrana.com.br</p>
      </footer>

      <div class="footer-band"></div>
    </div>
  </div>
</body>
</html>
```